THE QUIET LEDGER - "Trade" size book cover design for a novel

THE QUIET LEDGER is a thriller that explores what happens at THE QUIET LEDGER life and death. I'd like to see a cover that reflects the near death experience scenes, but I am open to any creative cover that reflects the theme of the book and the sample scenes that I have attached. Please read the scenes.
Space should be left on the cover for the typical promotional text, etc.

NOVEL SUMMARY - Dr. Pelham Rudnick is skeptical of the afterlife. He doesn't believe he will be reunited with his wife, or joined with God in heaven. What he knows, or thinks he knows, is that he should have seen the warning signs of his wife's heart attack, should have saved her. After four years of mourning, Pelham is finally moving on, succumbing to lust and longing, instead of sorrow. Still he fears the little mistakes that can kill, like a missed diagnosis, or the slip of a scalpel -- the kind of mistakes that depression feeds. When he dates the mother of an epileptic patient, he begins to believe that death will finally stop controlling his life. He has no idea, that the woman of his desires has killed her first husband, and will soon kill her son. As Pelham falls in love and marries, he also becomes involved in a clinical study of near death experiences. Life and research are about to collide.

The designs I have seen so far are quite dark and seem like they would better fit a horror novel. I am looking for something that is more beautiful. The near death experience scenes in the book are hopeful and wonderous. I also would prefer not to have a dark tunnel representing near death. Moths can also be beautiful creatures. I attached scenes from the book in the original post that might be helpful.

You don't have to use the moth as the focal point, or you might want to use moths as they appear in the main near death scene. I am not wedded to that idea.

Here are some additional ideas for designs: 1. At the climax of the book, there is a scene (see attachment) where there is a fight, and the main character's wife tries to kill him. In that scene, the main character breaks a picture frame with a Hercules Moth specimen over his wife's head. Perhaps a design could incorporate broken glass on the floor with the moth, in whole or part. It could even have a woman's foot wearing and athletic or bicycle shoe stepping on the glass. 2. In the scene where the main character has a near death experience (see attachment), there are vivid surreal descriptions of what he sees, including fluttering moths, numbers and colors. There are also visions of other souls represented as points of light. If this can be represented kind of like a representation of curvatures in space time, all the better. 3. When the main character is a boy, he is slightly autistic and is mesmerized by counting the leaves within a forest tall trees. That could be one possibility for a background. 4. When the main character and wife or on a bicycle vacation in Tuscany, they come across a vineyard after it rains. At the end of one of the vineyard rows, there is a beautiful multicolor rose bush. With droplets of water clinging to the petals. Perhaps there can be reflections in the water drops of moths, or something else (even if it is just light.)

Target Market(s)

Book Readers - Thrillers, suspense, near death experiences, medical(neurology).

Colors

Designer to choose colors to be used in the design.

Requirements
Must have
• Creative design that fits the theme of book. It should not be too dark and brooding (it is not a horror story.) It also should not look like a romance cover.
Nice to have
• One or more of the following as reflected in the attached scenes - Moths, (including Hercules moth); a silhouette of a middle aged bald man perhaps floating in the clouds, shards of broken glass from the picture frame in the climatic scene (not tempered glass from a windshield), near death graphics (not a dark tunnel), time/space or theoretical inspired graphic , the feeling of being caught between two worlds, tree canopy with lots of leaves; enlarged crystaline snow flakes each incorporating a symbol (such a pi, a circle with concentric octagons --ancient method of calculating area of circle, representations or pictures of moths, the symbol for infinity, shards of broken glass, prime numbers, bubbles of color. I am also not opposed to other abstract ideas.
Should not have
• Dark tunnels to represent near death.
• Romance novel cover or overly romantic.
• Horror type novel.

```html
<!DOCTYPE html>
<html lang="en">
<head>
<meta charset="utf-8">
<title>The Quiet Ledger — Cover</title>
<link rel="stylesheet" href="https://fonts.googleapis.com/css2?family=Cormorant+Garamond:wght@500&family=Kaushan+Script&family=Jost:wght@400&display=swap">
<style>
  :root {
    --paper: #d9d3a4;
    --paper-deep: #c9c28e;
    --panel: rgba(251, 250, 245, 0.84);
    --frame: #ffffff;
    --ink: #111111;
    --script: #6b5a33;
    --pulse: #1c1826;
    --rule: #c80a0a;
  }
  html, body {
    margin: 0;
    padding: 0;
    overflow: hidden;
    background: #ffffff;
  }
  .cover {
    position: relative;
    width: 800px;
    height: 1200px;
    overflow: hidden;
  }
  .cover__art {
    position: absolute;
    inset: 0;
    background: radial-gradient(ellipse at 50% 45%, var(--paper) 0%, var(--paper-deep) 100%);
  }
  .cover__pulse {
    position: absolute;
    inset: 0;
  }
  .cover__frame {
    position: absolute;
    left: 74px;
    top: 120px;
    width: 652px;
    height: 958px;
    box-sizing: border-box;
    border: 3px solid var(--frame);
  }
  .cover__panel {
    position: absolute;
    left: 82px;
    top: 129px;
    width: 636px;
    height: 940px;
    background: var(--panel);
  }
  .title {
    position: absolute;
    left: 0;
    top: 0;
    width: 800px;
    margin: 0;
    font-weight: normal;
  }
  .title__the {
    position: absolute;
    top: 178px;
    width: 800px;
    text-align: center;
    font-family: "Cormorant Garamond", serif;
    font-weight: 500;
    font-size: 100px;
    letter-spacing: 8px;
    color: var(--ink);
    line-height: 1;
  }
  .title__quiet {
    position: absolute;
    top: 300px;
    width: 800px;
    text-align: center;
    font-family: "Kaushan Script", cursive;
    font-size: 150px;
    color: var(--script);
    line-height: 1;
    transform: rotate(-9deg);
  }
  .title__ledger {
    position: absolute;
    top: 538px;
    width: 800px;
    text-align: center;
    font-family: "Cormorant Garamond", serif;
    font-weight: 500;
    font-size: 122px;
    letter-spacing: 2px;
    color: var(--ink);
    line-height: 1;
  }
  .cover__rule {
    position: absolute;
    left: 118px;
    top: 955px;
    width: 564px;
    height: 4px;
    background: var(--rule);
  }
  .cover__author {
    position: absolute;
    top: 985px;
    width: 800px;
    margin: 0;
    text-align: center;
    font-family: "Jost", sans-serif;
    font-size: 40px;
    color: var(--ink);
    line-height: 1;
  }
</style>
</head>
<body>
  <div class="cover">
    <div class="cover__art" role="img" aria-label="Watercolour moths and butterflies scattered over warm khaki paper"></div>

    <svg class="cover__pulse" width="800" height="1200" viewBox="0 0 800 1200" aria-hidden="true">
      <polyline points="0,792 146,792 168,665 212,1105 314,640 368,880 478,680 542,1000 614,792 800,792"
                fill="none" stroke="var(--pulse)" stroke-width="18" stroke-linejoin="miter" stroke-linecap="butt"/>
    </svg>

    <div class="cover__panel"></div>
    <div class="cover__frame"></div>

    <h1 class="title">
      <span class="title__the">the</span>
      <span class="title__quiet">Quiet</span>
      <span class="title__ledger">LEDGER</span>
    </h1>

    <div class="cover__rule"></div>
    <p class="cover__author">Autoh’s Name</p>
  </div>
</body>
</html>
```